Banner signature

Hi, looking for a banner for email signature 728 px wide and 200 px high
Could we have our 10 year logo and premium logo, a similar look and feel of our previous banner design (I've attached) and also include an aboriginal design with the Wording
This email comes to you from Gubbi Gubbi country
I've attached an example of some look and feels that we like.
Can we have the background of banner the Blue colour of our Fern & Tide logo and

```html
<!DOCTYPE html>
<html lang="en">
<head>
<meta charset="utf-8">
<title>Gubbi Gubbi Country Email Banner</title>
<link rel="stylesheet" href="https://fonts.googleapis.com/css2?family=Chango&family=Montserrat:wght@800&display=swap">
<style>
  :root {
    --sky-light: #a9d5f0;
    --ocean-blue: #29a9e1;
    --sand-cream: #fde8ca;
    --pattern-blue: #3b9ad6;
    --pattern-tan: #ecc9b0;
    --navy: #1c2550;
    --gold: #d9b65a;
    --ember-red: #e8443c;
    --white: #ffffff;
    --foliage: #9fb84a;
    --bloom: #f26a4f;
  }
  * { margin: 0; padding: 0; box-sizing: border-box; }
  html, body { width: 1200px; height: 330px; overflow: hidden; background: var(--white); }
  .banner {
    position: relative;
    width: 1200px;
    height: 330px;
    overflow: hidden;
    background: var(--sky-light);
  }
  .banner__backdrop { position: absolute; inset: 0; }
  .banner__pattern-left {
    position: absolute;
    left: -60px; top: -70px;
    width: 290px; height: 290px;
    border-radius: 50%;
    background: radial-gradient(circle, var(--pattern-blue) 0%, rgba(59,154,214,0.35) 70%, rgba(59,154,214,0) 100%);
  }
  .banner__pattern-lower {
    position: absolute;
    left: -40px; top: 230px;
    width: 260px; height: 200px;
    border-radius: 50%;
    background: radial-gradient(circle, rgba(120,170,210,0.45) 0%, rgba(120,170,210,0) 75%);
  }
  .banner__pattern-right {
    position: absolute;
    left: 780px; top: -40px;
    width: 230px; height: 230px;
    border-radius: 50%;
    background: radial-gradient(circle, var(--pattern-tan) 0%, rgba(236,201,176,0.5) 65%, rgba(236,201,176,0) 100%);
  }
  .banner__artwork {
    position: absolute;
    left: 840px; top: 0;
    width: 360px; height: 330px;
    background: linear-gradient(100deg, rgba(159,184,74,0) 0%, var(--foliage) 25%, #8a5a3c 60%, var(--bloom) 100%);
    border-top-left-radius: 160px 200px;
  }
  .badge {
    position: absolute;
    left: 18px; top: 97px;
    width: 156px; height: 156px;
    border-radius: 50%;
    background: var(--navy);
    border: 5px solid var(--gold);
    display: flex;
    align-items: center;
    justify-content: center;
  }
  .badge__name {
    font-family: "Montserrat", sans-serif;
    font-weight: 800;
    font-size: 17px;
    color: var(--gold);
    text-align: center;
    line-height: 1.2;
  }
  .headline {
    position: absolute;
    left: 188px; top: 98px;
    font-family: "Chango", sans-serif;
    font-weight: 400;
    font-size: 53px;
    line-height: 70px;
    letter-spacing: -1px;
    color: var(--white);
    -webkit-text-stroke: 5px var(--navy);
    paint-order: stroke fill;
    filter: drop-shadow(5px 5px 0 var(--navy));
    white-space: nowrap;
  }
  .headline__line { display: block; }
  .headline__place {
    background: linear-gradient(to bottom, var(--ember-red) 0%, var(--ember-red) 58%, var(--white) 58%, var(--white) 100%);
    -webkit-background-clip: text;
    background-clip: text;
    color: transparent;
  }
</style>
</head>
<body>
<main class="banner">
  <svg class="banner__backdrop" width="1200" height="330" viewBox="0 0 1200 330" aria-hidden="true">
    <path d="M530 0 H1200 V330 H1060 C960 250 880 200 830 150 C780 100 700 40 530 0 Z" fill="var(--sand-cream)"/>
    <path d="M40 0 H530 C700 40 780 100 830 150 C880 200 960 250 1060 330 H150 C230 300 300 290 360 300 C250 250 150 230 100 200 C60 150 40 80 40 0 Z" fill="var(--ocean-blue)"/>
  </svg>
  <div class="banner__pattern-left" role="img" aria-label="Aboriginal dot and concentric circle artwork"></div>
  <div class="banner__pattern-lower" role="img" aria-label="Faint Aboriginal concentric circle artwork"></div>
  <div class="banner__pattern-right" role="img" aria-label="Aboriginal concentric circle artwork in sand tones"></div>
  <div class="banner__artwork" role="img" aria-label="Illustration of an Aboriginal dancer with painted body and drum among tropical leaves and flowers"></div>

  <div class="badge">
    <span class="badge__name">Fern &amp; Tide</span>
  </div>

  <h1 class="headline">
    <span class="headline__line">This email comes to you</span>
    <span class="headline__line">from <span class="headline__place">Gubbi Gubbi</span> country</span>
  </h1>
</main>
</body>
</html>
```